Hawaiian fusion restaurant seeks new website design for upcoming 15th anniversary

We currently have a website-- kavoramesaplate.com-- but it's boring and we really want something exciting and fresh.

Coded - Design and coding required

1 page

Serif
Sans Serif

00AB8E
00BBA5
67D7C9
C6EFE9
E9F9F6
59FF00
82FF00
B8FF75
E3FFCB
F4FFEA
F0912C
F2A743
F7CA91
FBE8D2
FDF5EE

```html
<!DOCTYPE html>
<html lang="en">
<head>
<meta charset="utf-8">
<title>Kavora Mesa Grill</title>
<link rel="stylesheet" href="https://fonts.googleapis.com/css2?family=Trirong:wght@300;400&family=Poppins:wght@300;400;500&display=swap">
<style>
:root{
  --teal:#00ab8e;
  --teal-mid:#00bba5;
  --teal-light:#67d7c9;
  --teal-pale:#c6efe9;
  --teal-mist:#e9f9f6;
  --green:#59ff00;
  --lime:#82ff00;
  --orange:#f0912c;
  --amber:#f2a743;
  --peach:#f7ca91;
  --ink:#1b1b1b;
  --muted:#6c6c6c;
  --dark-brown:#1e1614;
  --charcoal:#2f2e33;
  --footer:#0d0d0d;
  --white:#ffffff;
}
*{box-sizing:border-box;margin:0;padding:0}
html,body{width:1200px;height:3462px;overflow:hidden}
body{position:relative;background:var(--white);font-family:"Poppins",sans-serif;color:var(--ink)}
.abs{position:absolute}
.serif{font-family:"Trirong",serif;font-weight:300}
.btn{position:absolute;display:flex;align-items:center;justify-content:center;gap:14px;border-radius:22px;font-size:15px;font-weight:400;color:var(--white)}
.btn svg{width:14px;height:14px}
.btn-teal{background:var(--teal)}
.btn-orange{background:var(--orange)}
.btn-amber{background:var(--amber);color:var(--ink)}

/* header */
.brand{position:absolute;left:159px;top:42px;display:flex;align-items:center;gap:8px;font-size:24px;font-weight:500;color:var(--teal)}
.brand-dot{width:16px;height:16px;border-radius:50%;background:var(--orange)}
.nav{position:absolute;left:521px;top:46px;display:flex;gap:33px;font-size:14px;color:var(--muted)}
.nav .active{color:var(--ink)}
.book{left:876px;top:34px;width:166px;height:43px;font-size:14px;font-weight:500;letter-spacing:.3px}

/* hero */
.hero-title{left:157px;top:190px;font-size:82px;line-height:76px;color:var(--teal)}
.hero-title span{display:block;color:var(--orange)}
.hero-lead{left:157px;top:354px;font-size:13px;color:var(--ink)}
.hero-copy{left:157px;top:388px;width:360px;font-size:12.5px;line-height:20px;color:var(--muted)}
.hero-photo{left:667px;top:185px;width:365px;height:511px;border-radius:90px 0 40px 0;background:linear-gradient(160deg,#3a3128,#1f1a14 60%,#4a3a26)}
.plate-a{left:940px;top:221px;width:190px;height:190px;border-radius:50%;background:radial-gradient(circle,#c98a4d 0 30%,#f4efe6 45%,#e3ddd2 70%);box-shadow:0 12px 30px rgba(0,0,0,.18)}
.plate-b{left:544px;top:396px;width:242px;height:242px;border-radius:50%;background:radial-gradient(circle,#8a3a2e 0 22%,#6c9a3a 40%,#f2f0ea 62%,#e0ddd6 75%);box-shadow:0 12px 30px rgba(0,0,0,.2)}
.view-tab{left:933px;top:528px;width:114px;height:97px;background:var(--teal);border-radius:0 30px 0 30px;color:var(--white);font-size:11px;line-height:13px;padding:38px 0 0 22px;display:flex;gap:14px}
.view-tab svg{width:12px;height:14px;margin-top:6px}

/* welcome */
.welcome{left:0;top:625px;width:1200px;height:625px;background:var(--dark-brown)}
.welcome-photo{left:0;top:625px;width:590px;height:625px;background:radial-gradient(circle at 45% 42%,#e8b06a 0 15%,#ece8e2 30%,#3a3836 45%,#2a2827)}
.welcome-title{left:600px;top:786px;font-size:37px;color:var(--white)}
.welcome-copy{left:603px;top:850px;width:375px;font-size:13px;line-height:18.8px;color:var(--white)}
.welcome-copy p+p{margin-top:18px}
.welcome-btn{left:603px;top:1027px;width:151px;height:40px}
.garlic{left:948px;top:1152px;width:170px;height:116px;border-radius:50% 50% 40% 40%;background:radial-gradient(circle at 60% 55%,#f1ece2,#d8cdbb 60%,transparent 72%)}

/* menu */
.menu-title{left:0;top:1345px;width:1200px;text-align:center;font-size:62px;color:var(--teal)}
.card{position:absolute;top:1448px;width:222px;text-align:center}
.card .dish{width:210px;height:210px;margin:0 auto;border-radius:50%;background:radial-gradient(circle,#d8582a 0 28%,#c74b24 40%,#f1efeb 58%,#e4e1dc 72%);box-shadow:0 8px 18px rgba(0,0,0,.12)}
.card h3{margin-top:24px;font-family:"Trirong",serif;font-weight:300;font-size:23px;color:var(--teal)}
.card p{margin-top:10px;font-size:13px;line-height:18.5px;color:var(--muted)}
.card-featured{left:715px;top:1545px;width:222px;height:276px;background:var(--teal-mist);border-radius:70px 0 0 0}
.card-link{left:804px;top:1807px;width:44px;height:44px;border-radius:50%;background:var(--white);box-shadow:0 3px 10px rgba(0,0,0,.15);display:flex;align-items:center;justify-content:center}
.menu-btn{left:524px;top:1866px;width:152px;height:40px}

/* tradition */
.tradition{left:0;top:1995px;width:1200px;height:564px;background:var(--charcoal)}
.tradition-photo{left:403px;top:1995px;width:797px;height:564px;background:radial-gradient(circle at 62% 57%,#c9552a 0 10%,#6a9a2e 20%,#1b1a1a 35%,#2c2a28 55%,#3a3530 80%,var(--charcoal))}
.tradition-title{left:159px;top:2130px;font-size:35px;line-height:44px;color:var(--white)}
.tradition-lead{left:159px;top:2236px;font-size:13px;color:var(--white)}
.tradition-copy{left:159px;top:2266px;width:375px;font-size:12.5px;line-height:18.8px;color:#d9d9d9}
.tradition-btn{left:159px;top:2390px;width:152px;height:40px}

/* testimonials */
.love-title{left:0;top:2662px;width:1200px;text-align:center;font-size:62px;color:var(--teal)}
.quote-mark{left:0;top:2762px;width:1200px;text-align:center;font-family:"Trirong",serif;font-weight:400;font-size:64px;line-height:48px;color:var(--orange)}
.quote{left:360px;top:2812px;width:480px;text-align:center;font-size:13px;line-height:20px;color:var(--muted)}
.quote strong{display:block;font-weight:400;color:var(--ink)}
.client{left:0;top:2906px;width:1200px;text-align:center;font-size:14px;color:var(--ink)}
.arrow-prev{left:192px;top:2818px}
.arrow-next{left:1000px;top:2818px}
.dots{left:574px;top:2960px;display:flex;gap:7px}
.dots i{width:8px;height:8px;border-radius:50%;background:#d6d6d6}
.dots i:first-child{background:var(--teal)}

/* footer */
.footer{left:0;top:3107px;width:1200px;height:355px;background:var(--footer)}
.footer-brand{left:159px;top:3215px;color:var(--teal-light)}
.footer-about{left:157px;top:3276px;width:200px;font-size:13px;line-height:20px;color:var(--white)}
.footer-about p+p{margin-top:14px}
.footer-col{position:absolute;top:3186px;font-size:12px;line-height:20px;color:var(--white)}
.footer-col h4{font-weight:400;font-size:17px;line-height:24px;margin-bottom:12px}
.footer-col p+p{margin-top:10px}
.links a{display:block;color:var(--white);text-decoration:none;line-height:27px;font-size:12px}
.email{left:870px;top:3226px;width:174px;height:33px;border:1px solid #555;border-radius:17px;padding:0 13px;font-size:11px;line-height:31px;color:#aaa}
.subscribe{left:870px;top:3271px;width:174px;height:31px;background:var(--orange);color:var(--ink);font-size:13px;letter-spacing:.5px}
.footer-rule{left:0;top:3408px;width:1200px;height:1px;background:#2b2b2b}
.copyright{left:0;top:3430px;width:1200px;text-align:center;font-size:11px;color:#8b8b8b}
</style>
</head>
<body>

<!-- header -->
<div class="brand"><span class="brand-dot"></span>Kavora Mesa</div>
<nav class="nav"><span class="active">Menu</span><span>Gallery</span><span>About us</span><span>Contact us</span></nav>
<div class="btn btn-teal book">BOOK A TABLE <svg viewBox="0 0 14 14"><path d="M1 7h11M8 3l4 4-4 4" fill="none" stroke="#fff" stroke-width="1.5"/></svg></div>

<!-- hero -->
<h1 class="abs serif hero-title">Good food<span>Great vibes</span></h1>
<p class="abs hero-lead">Sed ut perspiciatis unde omnis iste natus error sit vo</p>
<p class="abs hero-copy">accusantium doloremque laudantium, totam rem aperiam, eaque ab illo inventore veritatis et quasi architecto be.</p>
<div class="btn btn-teal" style="left:159px;top:466px;width:152px;height:42px">Order now <svg viewBox="0 0 14 14"><path d="M1 7h11M8 3l4 4-4 4" fill="none" stroke="#fff" stroke-width="1.5"/></svg></div>
<div class="btn btn-orange" style="left:324px;top:466px;width:149px;height:42px">Our menu <svg viewBox="0 0 14 14"><path d="M1 7h11M8 3l4 4-4 4" fill="none" stroke="#fff" stroke-width="1.5"/></svg></div>
<div class="abs hero-photo" role="img" aria-label="Dim restaurant dining room with wooden tables"></div>
<div class="abs plate-a" role="img" aria-label="Plate of fish cakes with lemon and dipping sauce"></div>
<div class="abs plate-b" role="img" aria-label="Seared tuna salad with chopsticks"></div>
<div class="abs view-tab"><span>View<br>our menu</span><svg viewBox="0 0 12 14"><path d="M3 1l6 6-6 6" fill="none" stroke="#fff" stroke-width="1.6"/></svg></div>

<!-- welcome -->
<section class="abs welcome"></section>
<div class="abs welcome-photo" role="img" aria-label="Papaya salad plate with eggs, limes, chillies and banana leaf on dark stone"></div>
<h2 class="abs serif welcome-title">Welcome to our cusine</h2>
<div class="abs welcome-copy">
  <p>When we opened Kavora Mesa Grill in September of 2007 our mission statement was simple: strive to serve delicious, fresh island flavors using wholesome, housemade products, local produce whenever possible, and take-out containers and utensils made from biocompostable plant fibers.</p>
  <p>We hope to see you soon. Mahalo!</p>
</div>
<div class="btn btn-amber welcome-btn">Order now <svg viewBox="0 0 14 14"><path d="M1 7h11M8 3l4 4-4 4" fill="none" stroke="#1b1b1b" stroke-width="1.5"/></svg></div>
<div class="abs garlic" role="img" aria-label="Garlic bulb with peppercorns"></div>

<!-- menu -->
<h2 class="abs serif menu-title">Our Menu</h2>
<div class="abs card-featured"></div>
<div class="card" style="left:-133px"><div class="dish" role="img" aria-label="Tuna salad bowl"></div><h3>Appetizer</h3><p>usantium doloremque laudantium, totam rem aperiam, eaque ab illo inventore veritatis et quasi</p></div>
<div class="card" style="left:151px"><div class="dish" role="img" aria-label="Stir-fried noodles with shrimp"></div><h3>Apitizer</h3><p>usantium doloremque laudantium, totam rem aperiam, eaque ab illo inventore veritatis et quasi</p></div>
<div class="card" style="left:422px"><div class="dish" role="img" aria-label="Papaya salad with lettuce"></div><h3>Salad</h3><p>usantium doloremque laudantium, totam rem aperiam, eaque ab illo inventore veritatis et quasi</p></div>
<div class="card" style="left:715px;top:1444px"><div class="dish" role="img" aria-label="Seafood curry with lime"></div><h3>Main course</h3><p>usantium doloremque laudantium, totam rem aperiam, eaque ab illo inventore veritatis et quasi</p></div>
<div class="card" style="left:990px;top:1444px"><div class="dish" role="img" aria-label="Fish cakes with sauce and lemon"></div><h3>Drinks</h3><p>usantium doloremque laudantium, totam rem aperiam, eaque ab illo inventore veritatis et quasi</p></div>
<div class="abs card-link"><svg width="22" height="22" viewBox="0 0 22 22"><circle cx="11" cy="11" r="9" fill="none" stroke="#00ab8e" stroke-width="1.6"/><path d="M6 11h9M11.5 7.5 15 11l-3.5 3.5" fill="none" stroke="#00ab8e" stroke-width="1.6"/></svg></div>
<div class="btn btn-teal menu-btn">View Menu <svg viewBox="0 0 14 14"><path d="M1 7h11M8 3l4 4-4 4" fill="none" stroke="#fff" stroke-width="1.5"/></svg></div>

<!-- tradition -->
<section class="abs tradition"></section>
<div class="abs tradition-photo" role="img" aria-label="Bowl of rice, broccoli and glazed chicken with chopsticks on a bamboo mat"></div>
<h2 class="abs serif tradition-title">Tradition &amp;<br>Family recipes</h2>
<p class="abs tradition-lead">Sed ut perspiciatis unde omnis iste natus error sit vo</p>
<p class="abs tradition-copy">Sed ut perspiciatis unde omnis iste natus error sit voluptatem accusantium doloremque laudantium, totam rem aperiam, eaque ipsa quae ab illo inventore veritatis et quasi architecto beatae vitae dicta sunt explicabo. Nemo enim ipsam voluptatem quia voluptas sit aspe</p>
<div class="btn btn-amber tradition-btn">About us <svg viewBox="0 0 14 14"><path d="M1 7h11M8 3l4 4-4 4" fill="none" stroke="#1b1b1b" stroke-width="1.5"/></svg></div>

<!-- testimonials -->
<h2 class="abs serif love-title">Why our client love us</h2>
<div class="abs quote-mark">&#8220;</div>
<p class="abs quote"><strong>Sed ut perspiciatis unde omnis iste natus error sit vo</strong>accusantium doloremque laudantium, totam rem aperiam, eaque ab illo inventore veritatis et quasi architecto be.</p>
<p class="abs client">- Client name</p>
<svg class="abs arrow-prev" width="22" height="14" viewBox="0 0 22 14"><path d="M21 7H2M7 1 1 7l6 6" fill="none" stroke="#888" stroke-width="1.3"/></svg>
<svg class="abs arrow-next" width="22" height="14" viewBox="0 0 22 14"><path d="M1 7h19M15 1l6 6-6 6" fill="none" stroke="#00ab8e" stroke-width="1.3"/></svg>
<div class="abs dots"><i></i><i></i><i></i><i></i></div>

<!-- footer -->
<footer class="abs footer"></footer>
<div class="brand footer-brand"><span class="brand-dot"></span>Kavora Mesa</div>
<div class="abs footer-about">
  <p style="font-weight:500">Proudly serving the Lanford community for 15 years!</p>
  <p>Our patio, dining room, and bar are open for seating.</p>
</div>
<div class="footer-col" style="left:421px">
  <h4>Address</h4>
  <p>Located at 21 Palmera Street in Lanford</p>
  <p style="margin-top:22px">Monday-Saturday 11am-8pm<br>Sunday 10am-8pm<br>Brunch served Sunday 10am-2pm</p>
  <p style="margin-top:22px">Happy Hour Daily from 3pm-6pm</p>
</div>
<div class="footer-col links" style="left:700px">
  <h4>Quick links</h4>
  <a href="#">Home</a><a href="#">About us</a><a href="#">Menu</a><a href="#">Gallery</a><a href="#">Order</a><a href="#">Contact us</a>
</div>
<div class="footer-col" style="left:874px"><h4>Newsletter subscribe</h4></div>
<div class="abs email">email id</div>
<div class="btn subscribe">SUBSCRIBE</div>
<div class="abs footer-rule"></div>
<p class="abs copyright">©Copyright 2022 | All rights reserved</p>

</body>
</html>
```